Genealogy Peer Study Group Website

Current site: Lineavault.org
New site:
* Optimized for mobile
* Will eliminate a few of the current pages
* Apply new colors and design (the new logo is already developed and colors are selected).
* The content is already created, as is the pages and desired navigation
* Current functionality that remains: directory, members-only access (private pages), enrollment form.
* New functionality - shopping cart (only one item is able to be purchased and it is a one-time purchase) and an brindle affiliate link to two books.
* Enhance directory to add more fields.
* The website updates (after development) must be able to be done by one of our volunteers and therefore coded with a commonly used technology.

Target Market(s)

Genealogy hobbyists. Mainly female, age range 30-70. U.S. based.

Coding

Coded - Design and coding required

Number of Pages Required

5+ page

Font styles to use
Other font styles liked:
• For the brand and logo, match the font on logo.

Colors
33a6d7

Requirements
Must have
• Match colors of the new logo that is included in the documents.

```html
<!DOCTYPE html>
<html lang="en">
<head>
<meta charset="utf-8">
<title>Lineavault Study Groups</title>
<link rel="stylesheet" href="https://fonts.googleapis.com/css2?family=Playfair+Display:wght@400;700&family=Montserrat:wght@400;500;600;700&display=swap">
<style>
:root{
  --blue:#33a6d7;
  --blue-dark:#2a6f95;
  --ink:#2b2b2b;
  --text:#555;
  --muted:#888;
  --footer:#222;
  --footer-2:#2b2b2b;
  --white:#fff;
  --line:#e4e4e4;
}
*{box-sizing:border-box;margin:0;padding:0}
html,body{width:1200px;height:3054px;overflow:hidden}
body{position:relative;font-family:'Montserrat',sans-serif;color:var(--text);background:var(--white)}
.abs{position:absolute}
.serif{font-family:'Playfair Display',serif}
.topbar{left:0;top:0;width:1200px;height:24px;border-bottom:1px solid var(--line);font-size:8px;color:var(--ink)}
.topbar .dot{position:absolute;top:8px;width:8px;height:8px;border-radius:50%;background:#333}
.header{left:0;top:24px;width:1200px;height:50px}
.brand{position:absolute;display:flex;align-items:center;gap:8px;font-family:'Montserrat',sans-serif;font-weight:600;color:var(--blue-dark)}
.brand .mark{border-radius:50%;background:var(--blue)}
.search{left:448px;top:20px;width:322px;height:18px;border-bottom:1px solid var(--line);font-size:8px}
.btn-outline{left:817px;top:16px;width:102px;height:19px;border:1.5px solid #333;font-size:7px;font-weight:600;text-align:center;line-height:16px;color:var(--ink)}
.nav{left:0;top:74px;width:1200px;height:31px;background:var(--blue);display:flex;justify-content:center;gap:28px;align-items:center}
.nav span{font-family:'Playfair Display',serif;color:var(--white);font-size:12px;margin:0 2px}
.hero{left:0;top:105px;width:1200px;height:559px;background:linear-gradient(180deg,#cfc7bd 0%,#9c7e5e 35%,#5b412b 65%,#2a2520 100%)}
.hero h1{position:absolute;top:262px;width:1200px;text-align:center;font-family:'Playfair Display',serif;font-weight:700;color:var(--white);font-size:54px;line-height:64px}
.hero p{position:absolute;top:398px;width:1200px;text-align:center;color:var(--white);font-size:15px}
.hero .b1{position:absolute;left:448px;top:434px;width:138px;height:30px;background:var(--blue);color:var(--white);font-size:8.5px;font-weight:600;text-align:center;line-height:30px}
.hero .b2{position:absolute;left:599px;top:434px;width:150px;height:30px;border:1.5px solid var(--white);color:var(--white);font-size:8.5px;font-weight:600;text-align:center;line-height:27px}
.card{top:713px;width:225px;height:207px}
.card span{position:absolute;left:17px;bottom:28px;color:var(--white);font-family:'Playfair Display',serif;font-weight:700;font-size:16px}
.card i{position:absolute;left:17px;bottom:18px;width:24px;height:1px;background:var(--white)}
h2{font-family:'Playfair Display',serif;font-weight:700;color:var(--ink)}
.small{font-size:8.5px;line-height:15px;color:var(--text)}
.ticks li{list-style:none;position:relative;padding-left:33px}
.ticks svg{position:absolute;left:0;top:0}
.elements{left:0;top:1240px;width:1200px;height:449px}
.footer{left:0;top:2787px;width:1200px;height:267px;background:var(--footer)}
.footer .col{font-size:8.5px;color:#ddd;line-height:25px;font-weight:500}
</style>
</head>
<body>

<div class="abs topbar">
  <i class="dot" style="left:232px"></i><i class="dot" style="left:248px"></i>
  <span class="abs" style="left:285px;top:7px">Need Help? call: 0800 555 0142</span>
  <span class="abs" style="left:802px;top:7px">SUPPORT</span>
  <span class="abs" style="left:858px;top:7px">LOG IN</span>
  <span class="abs" style="left:910px;top:7px">◎&nbsp; Languages</span>
</div>

<div class="abs header">
  <div class="brand" style="left:234px;top:8px;font-size:15px">Lineavault<span class="mark" style="width:32px;height:32px"></span></div>
  <div class="abs search">&#9906;</div>
  <div class="abs btn-outline">GET IN TOUCH</div>
  <svg class="abs" style="left:936px;top:13px" width="30" height="22" viewBox="0 0 30 22" fill="none" stroke="#333" stroke-width="1.4"><path d="M2 6h26l-3 14H5z"/><path d="M9 6l3-5M21 6l-3-5"/></svg>
</div>

<nav class="abs nav"><span>Home</span><span>Program</span><span>About</span><span>Directory</span><span>Alumni</span><span>Contact</span></nav>

<section class="abs hero" role="img" aria-label="Photo of a grand domed library reading room with bookshelves and readers">
  <svg class="abs" style="left:77px;top:292px" width="14" height="26" fill="none" stroke="#fff" stroke-width="2"><path d="M12 2L2 13l10 11"/></svg>
  <span class="abs" style="left:1076px;top:302px;color:#fff;font-size:6px">NEXT</span>
  <svg class="abs" style="left:1102px;top:292px" width="14" height="26" fill="none" stroke="#fff" stroke-width="2"><path d="M2 2l10 11L2 24"/></svg>
  <h1>Encouraging Professional<br>&amp; Aspiring Genealogists</h1>
  <p>The Lineavault Study Groups are organized to encourage professional and aspiring genealogists.</p>
  <div class="b1">Browse Directory</div>
  <div class="b2">Show All Events</div>
</section>

<div class="abs card" style="left:235px;background:linear-gradient(160deg,#6c6f78,#2d2b2e)" role="img" aria-label="Photo of the group administrator speaking"><span>Lineavault Administrator</span><i></i></div>
<div class="abs card" style="left:487px;background:linear-gradient(160deg,#8c918f,#2b2d30)" role="img" aria-label="Photo of the coordinators team standing together"><span>Lineavault Coordinator</span><i></i></div>
<div class="abs card" style="left:740px;background:linear-gradient(160deg,#cdbfae,#3a3534)" role="img" aria-label="Photo of the group leader seated in thought"><span>Lineavault Leader</span><i></i></div>

<div class="abs" style="left:234px;top:951px;width:478px;height:240px;background:linear-gradient(150deg,#e8e6df,#9b9488 60%,#3b3633)" role="img" aria-label="Photo of an instructor presenting to a seated study group"></div>
<h2 class="abs" style="left:740px;top:967px;font-size:16px">Lineavault Study Groups Are</h2>
<p class="abs small" style="left:740px;top:1006px;width:228px">The Lineavault Study Groups are organized to support both professional and aspiring genealogists enhance their existing research methods as well as to create good business practices. Lineavault is a self-study program enhanced by peer review of assignments based on chapters from Practical Lineage Research: Preparation, Practice &amp; Standards, edited by Margaret Ellery Haines.</p>
<div class="abs" style="left:740px;top:1140px;width:173px;height:33px;background:var(--blue-dark);color:#fff;font-size:8.5px;font-weight:600;text-align:center;line-height:33px">READ MORE</div>

<section class="abs elements">
  <div class="abs" style="left:0;top:0;width:599px;height:449px;background:linear-gradient(140deg,#6b5f52,#d9d5cf 45%,#a37f5c 80%,#7a5a3d)" role="img" aria-label="Photo of a person working on a laptop at a wooden desk with books"></div>
  <div class="abs" style="left:599px;top:0;width:601px;height:449px;background:var(--blue)">
    <h2 class="abs" style="left:53px;top:83px;font-size:16px;line-height:20px;color:#fff">Key Elements of the Lineavault<br>Study Program</h2>
    <ul class="abs ticks" style="left:53px;top:150px;color:#fff;font-size:9px;line-height:14px">
      <li style="height:43px"><svg width="20" height="20" fill="none" stroke="#fff" stroke-width="1.6"><rect x="1" y="4" width="15" height="15"/><path d="M4 11l4 5L19 1"/></svg>Quality textbooks (Practical Lineage Research &amp; Sources Made Clear)<br>written by experts in the field</li>
      <li style="height:37px"><svg width="20" height="20" fill="none" stroke="#fff" stroke-width="1.6"><rect x="1" y="4" width="15" height="15"/><path d="M4 11l4 5L19 1"/></svg>Monthly assignments crafted to maximize learning</li>
      <li style="height:37px"><svg width="20" height="20" fill="none" stroke="#fff" stroke-width="1.6"><rect x="1" y="4" width="15" height="15"/><path d="M4 11l4 5L19 1"/></svg>Written peer feedback</li>
      <li style="height:37px"><svg width="20" height="20" fill="none" stroke="#fff" stroke-width="1.6"><rect x="1" y="4" width="15" height="15"/><path d="M4 11l4 5L19 1"/></svg>Live monthly video chats reviewing each topic</li>
      <li style="height:37px"><svg width="20" height="20" fill="none" stroke="#fff" stroke-width="1.6"><rect x="1" y="4" width="15" height="15"/><path d="M4 11l4 5L19 1"/></svg>Guidance from a Certified Genealogist or an Accredited Genealogist</li>
      <li><svg width="20" height="20" fill="none" stroke="#fff" stroke-width="1.6"><rect x="1" y="4" width="15" height="15"/><path d="M4 11l4 5L19 1"/></svg>14-month study program</li>
    </ul>
  </div>
</section>

<h2 class="abs" style="left:0;top:1736px;width:1200px;text-align:center;font-size:16px">What Lineavault Alumni Are Saying</h2>
<div class="abs" style="left:427px;top:1780px;width:347px;height:75px;background:#fff;box-shadow:0 2px 12px rgba(0,0,0,.1);text-align:center;padding-top:21px;font-size:13.5px;line-height:22px;color:#777">
  <span class="abs serif" style="left:45px;top:2px;color:var(--blue);font-size:26px;font-weight:700">&ldquo;</span>
  Lineavault was great for my genealogy<br>education journey...
</div>
<svg class="abs" style="left:333px;top:1866px" width="12" height="22" fill="none" stroke="#999" stroke-width="1.5"><path d="M10 1L2 11l8 10"/></svg>
<span class="abs" style="left:832px;top:1873px;font-size:6px;color:#aaa;background:#eee;padding:0 2px">NEXT</span>
<svg class="abs" style="left:858px;top:1866px" width="12" height="22" fill="none" stroke="#666" stroke-width="1.5"><path d="M2 1l8 10-8 10"/></svg>
<div class="abs" style="left:474px;top:1870px;width:78px;height:78px;border-radius:50%;background:linear-gradient(160deg,#c9b8a8,#6a5446)" role="img" aria-label="Portrait of the alumna"></div>
<div class="abs serif" style="left:569px;top:1888px;font-size:15px;font-weight:700;color:var(--ink)">Dana Whitlow</div>
<div class="abs" style="left:569px;top:1917px;font-size:9.5px;color:#888">From <b style="color:#555">UK</b></div>

<div class="abs" style="left:235px;top:1997px;width:356px;height:323px;background:linear-gradient(150deg,#e9ecef,#c4c7cb 50%,#3d3a3e)" role="img" aria-label="Photo of three professionals meeting at a table with laptops"></div>
<h2 class="abs" style="left:608px;top:2020px;font-size:16px">Is Lineavault Right for Me?</h2>
<p class="abs" style="left:608px;top:2053px;font-size:12px;color:#666">The Lineavault Study Groups may be right for you if...</p>
<ul class="abs ticks small" style="left:608px;top:2093px;width:360px">
  <li style="height:42px"><svg width="20" height="20" fill="none" stroke="var(--blue)" stroke-width="1.5"><rect x="1" y="4" width="15" height="15"/><path d="M4 11l4 5L19 1"/></svg>You want to become a professional genealogist researching for others</li>
  <li style="height:53px;line-height:19px"><svg width="20" height="20" fill="none" stroke="var(--blue)" stroke-width="1.5"><rect x="1" y="4" width="15" height="15"/><path d="M4 11l4 5L19 1"/></svg>You already research professionally and want to learn more about managing your business or presenting your written work.</li>
  <li style="height:38px"><svg width="20" height="20" fill="none" stroke="var(--blue)" stroke-width="1.5"><rect x="1" y="4" width="15" height="15"/><path d="M4 11l4 5L19 1"/></svg>Improving your research skills is important to you.</li>
  <li style="height:37px"><svg width="20" height="20" fill="none" stroke="var(--blue)" stroke-width="1.5"><rect x="1" y="4" width="15" height="15"/><path d="M4 11l4 5L19 1"/></svg>You are considering becoming credentialed or accredited.</li>
  <li><svg width="20" height="20" fill="none" stroke="var(--blue)" stroke-width="1.5"><rect x="1" y="4" width="15" height="15"/><path d="M4 11l4 5L19 1"/></svg>Researching to your best ability for yourself is your goal.</li>
</ul>

<h2 class="abs" style="left:234px;top:2391px;font-size:16px">Am I Right for Lineavault?</h2>
<p class="abs" style="left:234px;top:2424px;font-size:12px;color:#666">You may be right for the Lineavault Study Groups if you...</p>
<ul class="abs ticks small" style="left:234px;top:2464px;width:340px">
  <li style="height:43px"><svg width="20" height="20" fill="none" stroke="var(--blue)" stroke-width="1.5"><rect x="1" y="4" width="15" height="15"/><path d="M4 11l4 5L19 1"/></svg>Have practiced genealogy research for several years.</li>
  <li style="height:92px;line-height:19px"><svg width="20" height="20" fill="none" stroke="var(--blue)" stroke-width="1.5"><rect x="1" y="4" width="15" height="15"/><path d="M4 11l4 5L19 1"/></svg>Successfully participated and completed courses such as the Northfield College Certificate in Genealogical Research, the National Lineage Society Foundations Course, or intermediate level courses at institutes such as RLI, HRW or SGS.</li>
  <li><svg width="20" height="20" fill="none" stroke="var(--blue)" stroke-width="1.5"><rect x="1" y="4" width="15" height="15"/><path d="M4 11l4 5L19 1"/></svg>Demonstrate strong research skills in your daily work.</li>
</ul>
<div class="abs" style="left:608px;top:2371px;width:357px;height:279px;background:linear-gradient(150deg,#7c7a70,#d8d6d0 50%,#4a4a46)" role="img" aria-label="Photo of a senior man in shirt and tie seated at a desk"></div>

<section class="abs" style="left:0;top:2700px;width:1200px;height:87px;background:var(--blue)">
  <h2 class="abs" style="left:251px;top:31px;font-size:18px;color:#fff">Subscribe to Our Newsletter</h2>
  <div class="abs" style="left:505px;top:27px;width:348px;height:34px;border:1px solid #fff;color:#fff;font-size:9px;line-height:32px;padding-left:45px">Type Your Email Address</div>
  <div class="abs" style="left:853px;top:27px;width:95px;height:34px;background:#fff;color:var(--ink);font-size:10.5px;font-weight:700;text-align:center;line-height:34px">SUBSCRIBE</div>
</section>

<footer class="abs footer">
  <div class="abs" style="left:744px;top:0;width:456px;height:267px;background:var(--footer-2)"></div>
  <div class="abs col" style="left:235px;top:38px">HOME<br>DIRECTORY<br>EVENTS</div>
  <div class="abs col" style="left:398px;top:38px">LEADERSHIP<br>ENROLL<br>GALLERY</div>
  <div class="abs" style="left:560px;top:45px;font-size:8.5px;color:#ddd;font-weight:600">OTHER STUDY GROUPS</div>
  <div class="abs" style="left:560px;top:66px;font-size:8.5px;line-height:15px;color:#999">Quarterly Review Study Group<br>Proof Argument Study Group</div>
  <div class="brand" style="left:830px;top:30px;font-size:17px;color:var(--blue)">Lineavault<span class="mark" style="width:54px;height:54px"></span></div>
  <div class="abs" style="left:700px;top:110px;width:266px;text-align:right;font-size:8.5px;line-height:16px;color:#eee">48 Harbor Row, Suite 210,<br>Millbrook, OR 97000, USA</div>
  <span class="abs" style="left:921px;top:168px;width:19px;height:19px;border-radius:50%;background:#fff"></span>
  <span class="abs" style="left:946px;top:168px;width:19px;height:19px;border-radius:50%;background:#fff"></span>
  <div class="abs" style="left:235px;top:227px;font-size:8px;line-height:19px;color:#ddd">Copyright @ 2020 - Helen Marsh Corbett. &nbsp;&nbsp;All Rights Reserved.<br>Privacy Policy &nbsp;|&nbsp; Terms of Use</div>
  <div class="abs" style="left:700px;top:246px;width:263px;text-align:right;font-size:8px;color:#ddd">Powered by: Fernleaf Web Studio</div>
  <div class="abs" style="left:1164px;top:226px;width:36px;height:41px;background:var(--blue);clip-path:polygon(100% 0,100% 100%,0 100%,0 40%)"></div>
  <svg class="abs" style="left:1177px;top:244px" width="10" height="6" fill="none" stroke="#fff" stroke-width="1.4"><path d="M1 5l4-4 4 4"/></svg>
  <span class="abs" style="left:1174px;top:254px;font-size:6.5px;color:#fff;font-weight:600">TOP</span>
</footer>

</body>
</html>
```